KT-Systems advertising flag and billboard design

I need a design for advertising flag and a design for billboard.
Information can be obtained from https://kt-sytronik.de.
Updates
Target Market(s)
IT service for companies
Requirements
Must have
- Logo, contact information and services

```html
<!DOCTYPE html>
<html lang="en">
<head>
<meta charset="utf-8">
<title>KT-Systems Billboard</title>
<link rel="stylesheet" href="https://fonts.googleapis.com/css2?family=Montserrat:wght@600;700&family=Archivo+Black&family=Russo+One&display=swap">
<style>
  :root {
    --page-bg: #ccc9c9;
    --panel-black: #000000;
    --brand-blue: #0a0ad6;
    --text-white: #ffffff;
    --logo-silver: #e4e4e4;
    --strip-light: #e9e7e7;
    --strip-dark: #8f8f8f;
    --photo-navy: #1b2a44;
    --photo-teal: #4f8ea3;
    --photo-skin: #a8745a;
  }
  * { margin: 0; padding: 0; box-sizing: border-box; }
  html, body {
    width: 1047px;
    height: 1200px;
    overflow: hidden;
    background: var(--page-bg);
  }
  .billboard {
    position: absolute;
    left: 34px;
    top: 457px;
    width: 980px;
    height: 286px;
    background: var(--panel-black);
    overflow: hidden;
    box-shadow: 0 8px 14px rgba(0,0,0,0.45);
    font-family: "Montserrat", sans-serif;
    color: var(--text-white);
  }
  .billboard__photo {
    position: absolute;
    left: 420px;
    top: 0;
    width: 560px;
    height: 286px;
    background:
      radial-gradient(ellipse 120px 70px at 52% 52%, var(--photo-skin), transparent 75%),
      radial-gradient(ellipse 160px 110px at 85% 30%, var(--photo-teal), transparent 80%),
      linear-gradient(90deg, var(--panel-black) 0%, var(--photo-navy) 30%, #2c4a5c 70%, #6b5a4c 100%);
  }
  .billboard__photo::before {
    content: "";
    position: absolute;
    inset: 0;
    background: linear-gradient(90deg, var(--panel-black) 0%, rgba(0,0,0,0) 35%);
  }
  .brand-name {
    position: absolute;
    left: 23px;
    top: 18px;
    font-weight: 700;
    font-size: 38px;
    letter-spacing: 1px;
    color: var(--logo-silver);
    line-height: 1;
  }
  .services-tag {
    position: absolute;
    left: 23px;
    top: 73px;
    height: 27px;
    padding: 0 12px;
    border-radius: 14px;
    background: var(--brand-blue);
    font-weight: 700;
    font-size: 20px;
    line-height: 27px;
    color: var(--text-white);
  }
  .services-list {
    position: absolute;
    top: 107px;
    list-style: none;
    font-weight: 600;
    font-size: 16px;
    line-height: 26px;
  }
  .services-list--left { left: 23px; }
  .services-list--right { left: 303px; }
  .services-list li::before {
    content: "";
    display: inline-block;
    width: 7px;
    height: 7px;
    border-radius: 50%;
    background: var(--text-white);
    margin-right: 5px;
    vertical-align: 2px;
  }
  .footer-shapes {
    position: absolute;
    left: 0;
    top: 0;
  }
  .website {
    position: absolute;
    left: 23px;
    top: 255px;
    font-family: "Archivo Black", sans-serif;
    font-size: 18px;
    letter-spacing: 6.5px;
    color: #111111;
    line-height: 26px;
  }
  .phone {
    position: absolute;
    right: 24px;
    top: 237px;
    font-family: "Russo One", sans-serif;
    font-size: 34px;
    letter-spacing: 1px;
    color: var(--text-white);
    line-height: 40px;
  }
</style>
</head>
<body>
  <section class="billboard">
    <div class="billboard__photo" role="img" aria-label="Photo of two business people in suits shaking hands in front of a blurred office with bokeh lights"></div>

    <div class="brand-name">KT-SYSTEMS</div>

    <div class="services-tag">OUR SERVICES</div>

    <ul class="services-list services-list--left">
      <li>Laptop Reparatur</li>
      <li>PC Reparatur</li>
      <li>Mac Reparatur</li>
      <li>Data Backup and Recovery</li>
      <li>Malware and Virus Entfernen</li>
    </ul>

    <ul class="services-list services-list--right">
      <li>Software Installation</li>
      <li>Hardware Upgrade</li>
      <li>PC Individuell</li>
      <li>Network / Servers</li>
    </ul>

    <svg class="footer-shapes" width="980" height="286" viewBox="0 0 980 286" aria-hidden="true">
      <defs>
        <linearGradient id="strip-gradient" x1="0" y1="0" x2="1" y2="0">
          <stop offset="0" stop-color="var(--strip-dark)"/>
          <stop offset="0.35" stop-color="var(--strip-light)"/>
          <stop offset="1" stop-color="#cfcdcd"/>
        </linearGradient>
      </defs>
      <polygon points="0,250 539,250 500,286 0,286" fill="url(#strip-gradient)"/>
      <path d="M500,286 L553,235 Q562,225 578,225 L980,225 L980,286 Z" fill="var(--brand-blue)"/>
    </svg>

    <div class="website">www.kt-sytronik.de</div>
    <div class="phone">01234-5678901</div>
  </section>
</body>
</html>
```